Gift card design to reflect the theme from our overhead business sign

We need a gift card that aligns with our colors used for the sign. Since I am not sure what you're able to do with the limited space, if you think you can create a miniature version of the sign and add the words "Gift Card" to it. I'd like to see it. I have also uploaded the original logo we use as an other variable to use in place the horizontal one on the sign. That might be alright too. Give me a few options to consider.

Then for the back of the card there may be some legal requirements for the wording. I'll get back to you on that. First, let's focus on the design.

Also, i am sending the requirements for "Tormix" who will be the processor for the card. I will be doing custom cards so pay attention to page 4.

After the gift card, I will sending you the front of the store image with the sign in place, so you can come up with some ideas for a simple window design to go across all the windows.

How fast can you get back to me? Unlike the sign, I'm sort of in a time crunch.

Oh, one other thing, I want to change the pink in our current logo to the pink you used in the sign. So if you use our standard logo, please change the pink to the on you used for the sign.

```html
<!DOCTYPE html>
<html lang="en">
<head>
<meta charset="utf-8">
<title>The Crumb Parlor Gift Card</title>
<link rel="stylesheet" href="https://fonts.googleapis.com/css2?family=Fredoka:wght@600&display=swap">
<style>
  :root {
    --card-pink: #ec3b94;
    --shadow-plum: #b3286c;
    --lime: #a5d13f;
    --white: #ffffff;
  }
  html, body {
    margin: 0;
    padding: 0;
    width: 1200px;
    height: 785px;
    overflow: hidden;
    background: var(--card-pink);
  }
  .gift-card {
    position: relative;
    width: 1200px;
    height: 785px;
    background: var(--card-pink);
    overflow: hidden;
    font-family: "Fredoka", "Varela Round", sans-serif;
  }
  .ribbon {
    position: absolute;
    left: 0;
    top: 0;
  }
  .brand {
    position: absolute;
    left: 110px;
    top: 92px;
    width: 800px;
    color: var(--white);
  }
  .brand-name {
    margin: 0;
    font-weight: 600;
    font-size: 100px;
    line-height: 1;
    letter-spacing: -1px;
    white-space: nowrap;
  }
  .brand-tagline {
    margin: 22px 0 0 4px;
    font-weight: 600;
    font-size: 40px;
    line-height: 1;
    white-space: nowrap;
  }
  .card-title {
    position: absolute;
    left: 237px;
    top: 478px;
    margin: 0;
    font-weight: 600;
    font-size: 130px;
    line-height: 1;
    color: var(--lime);
    white-space: nowrap;
    text-shadow: 10px 10px 0 var(--shadow-plum);
  }
</style>
</head>
<body>
  <main class="gift-card">
    <svg class="ribbon" width="1200" height="785" viewBox="0 0 1200 785">
      <defs>
        <linearGradient id="band-horizontal" x1="0" y1="0" x2="1" y2="0">
          <stop offset="0" stop-color="#fbb874"/>
          <stop offset="0.6" stop-color="#f9a55a"/>
          <stop offset="1" stop-color="#f26a1f"/>
        </linearGradient>
        <linearGradient id="band-vertical" x1="0" y1="0" x2="0" y2="1">
          <stop offset="0" stop-color="#f26a1f"/>
          <stop offset="0.4" stop-color="#f68f3a"/>
          <stop offset="1" stop-color="#f47f2c"/>
        </linearGradient>
        <linearGradient id="bow-tone" x1="0" y1="0" x2="1" y2="1">
          <stop offset="0" stop-color="#fbb874"/>
          <stop offset="0.5" stop-color="#f68f3a"/>
          <stop offset="1" stop-color="#f05f1c"/>
        </linearGradient>
      </defs>
      <rect class="ribbon-band-vertical" x="951" y="0" width="80" height="785" fill="url(#band-vertical)"/>
      <rect class="ribbon-band-horizontal" x="0" y="351" width="1200" height="99" fill="url(#band-horizontal)"/>
      <rect class="ribbon-bow" role="img" aria-label="Orange satin ribbon bow tied where the bands cross"
            x="846" y="332" width="296" height="242" rx="40" fill="url(#bow-tone)"/>
    </svg>

    <header class="brand">
      <p class="brand-name">The Crumb Parlor</p>
      <p class="brand-tagline">fresh bakes daily</p>
    </header>

    <h1 class="card-title">Gift Card</h1>
  </main>
</body>
</html>
```